Milo Fenwick - Cinematographer

NEED:
I'm looking for a sleek, professional, modern business card that will give give the recipient the impression that they can trust their production will go smoothly by hiring me. I will bring creativity and knowledge to their shoot, so that we can create powerful images.
I am looking for a card with a strong style and design ethos that could be expanded to a website and a full visual/graphic/design entity for me.
ABOUT ME:
I am a mid-twenties cinematographer, I work on music video, narrative short, commercial, and corporate projects. I blend the science and artistry of cameras and filmmaking to tell a story. I'm an artist, a technician, and a manager.
DESIGN:
I like sleek, simple design. Black, dark grays, white, dark navy, steel blues, I love cyan, but also cyan and red. I am not a fan of earthy tones. I generally prefer modern, san-serif fonts over serifs. My old logo was based on an aperture, a multi-blade device at the back of a lens that controls how much light passes through, but I made it with so many colors, that it doesn't necessarily lend itself to a specific color-scheme or design ethos. I liked that the aperture design provided a sense of the technical requirements of my job. I'm a fan of matte business cards, but am open to plenty of specialty print processes to make an outstanding card.
ATTACHED FILES:
My Old Rainbox Aperture Logo, plus a few designs I've tried playing around with, but am not tied to. I AM OPEN TO NEW DESIGNS, DO NOT FEEL TIED TO THIS.
**I've pulled my old logo down from the attached files, and instead attached other business cards I like, so as not to mislead you where I would like to go.
INFO:
Name: Milo Fenwick
Job: Cinematographer
Email: mpfenwick@quellbox.net
Phone: 415.555.0193
Website: milofenwick.net
I'm adding some images of other cards that I like, and removing my old logo, since I'm looking for something new, and don't want that old logo to push anyone a certain direction.

```html
<!DOCTYPE html>
<html lang="en">
<head>
<meta charset="utf-8">
<title>Milo Fenwick – Cinematographer Business Card</title>
<link rel="stylesheet" href="https://fonts.googleapis.com/css2?family=Montserrat:wght@300;700&family=Open+Sans:wght@400;700&display=swap">
<style>
  :root {
    --page-bg: #d9d9db;
    --card-black: #0d0d0e;
    --card-charcoal: #242426;
    --text-white: #ffffff;
    --text-soft: #e4e4e6;
    --accent-cyan: #2bb8e6;
    --icon-blue: #2f8fdc;
  }
  * { margin: 0; padding: 0; box-sizing: border-box; }
  html, body { width: 1200px; height: 913px; overflow: hidden; }
  body {
    background: var(--page-bg);
    display: flex;
    flex-direction: column;
    align-items: center;
    justify-content: center;
    gap: 48px;
    font-family: "Open Sans", Arial, sans-serif;
  }
  .card {
    position: relative;
    width: 690px;
    height: 394px;
    border-radius: 6px;
    background: linear-gradient(135deg, var(--card-charcoal) 0%, var(--card-black) 70%);
    box-shadow: 0 10px 28px rgba(0, 0, 0, 0.28);
    overflow: hidden;
    color: var(--text-white);
  }

  /* Front */
  .card-front .lockup {
    position: absolute;
    left: 200px;
    top: 96px;
    width: 300px;
    height: 210px;
  }
  .lockup .mark-circle {
    position: absolute;
    left: 70px;
    top: 0;
    width: 160px;
    height: 160px;
    border-radius: 50%;
    background: var(--accent-cyan);
  }
  .lockup .brand-name {
    position: absolute;
    left: -40px;
    right: -40px;
    top: 128px;
    text-align: center;
    font-family: "Montserrat", Arial, sans-serif;
    font-weight: 700;
    font-size: 40px;
    letter-spacing: 1px;
    color: var(--text-white);
    text-transform: uppercase;
  }
  .lockup .brand-role {
    position: absolute;
    left: -40px;
    right: -40px;
    top: 180px;
    text-align: center;
    font-family: "Montserrat", Arial, sans-serif;
    font-weight: 300;
    font-size: 20px;
    letter-spacing: 6px;
    color: var(--text-soft);
    text-transform: uppercase;
  }

  /* Back */
  .card-back .lockup-small {
    position: absolute;
    left: 60px;
    top: 110px;
    width: 220px;
    height: 180px;
  }
  .lockup-small .mark-circle {
    position: absolute;
    left: 55px;
    top: 0;
    width: 110px;
    height: 110px;
    border-radius: 50%;
    background: var(--accent-cyan);
  }
  .lockup-small .brand-name {
    position: absolute;
    left: -20px;
    right: -20px;
    top: 92px;
    text-align: center;
    font-family: "Montserrat", Arial, sans-serif;
    font-weight: 700;
    font-size: 26px;
    letter-spacing: 1px;
    text-transform: uppercase;
    color: var(--text-white);
  }
  .lockup-small .brand-role {
    position: absolute;
    left: -20px;
    right: -20px;
    top: 128px;
    text-align: center;
    font-family: "Montserrat", Arial, sans-serif;
    font-weight: 300;
    font-size: 13px;
    letter-spacing: 4px;
    text-transform: uppercase;
    color: var(--text-soft);
  }
  .contact-block {
    position: absolute;
    left: 360px;
    top: 112px;
  }
  .contact-block .person-name {
    font-weight: 700;
    font-size: 26px;
    line-height: 1.2;
  }
  .contact-block .person-role {
    font-weight: 700;
    font-size: 15px;
    color: var(--text-soft);
    margin-top: 6px;
    margin-bottom: 22px;
  }
  .contact-list { list-style: none; }
  .contact-list li {
    display: flex;
    align-items: center;
    gap: 12px;
    font-size: 17px;
    color: var(--text-soft);
    line-height: 30px;
  }
  .contact-list svg { width: 18px; height: 18px; flex: none; }
</style>
</head>
<body>

  <section class="card card-front" aria-label="Business card front">
    <div class="lockup">
      <div class="mark-circle"></div>
      <div class="brand-name">Milo Fenwick</div>
      <div class="brand-role">Cinematographer</div>
    </div>
  </section>

  <section class="card card-back" aria-label="Business card back">
    <div class="lockup-small">
      <div class="mark-circle"></div>
      <div class="brand-name">Milo Fenwick</div>
      <div class="brand-role">Cinematographer</div>
    </div>

    <div class="contact-block">
      <div class="person-name">Milo Fenwick</div>
      <div class="person-role">Cinematographer</div>
      <ul class="contact-list">
        <li>
          <svg viewBox="0 0 20 20" aria-hidden="true">
            <rect x="1" y="4" width="18" height="12" rx="1.5" fill="var(--icon-blue)"/>
            <path d="M2 5 L10 11 L18 5" fill="none" stroke="#0d0d0e" stroke-width="1.5"/>
          </svg>
          mpfenwick@quellbox.net
        </li>
        <li>
          <svg viewBox="0 0 20 20" aria-hidden="true">
            <path d="M2 7 Q10 1 18 7 L16 9 L13 7.5 L13 6 Q10 5 7 6 L7 7.5 L4 9 Z" fill="var(--icon-blue)"/>
            <rect x="4" y="10" width="12" height="7" rx="1.5" fill="var(--icon-blue)"/>
          </svg>
          415.555.0193
        </li>
        <li>
          <svg viewBox="0 0 20 20" aria-hidden="true">
            <circle cx="10" cy="10" r="8" fill="var(--icon-blue)"/>
            <g fill="none" stroke="#0d0d0e" stroke-width="1.1">
              <ellipse cx="10" cy="10" rx="3.5" ry="8"/>
              <line x1="2" y1="10" x2="18" y2="10"/>
              <line x1="3.5" y1="6" x2="16.5" y2="6"/>
              <line x1="3.5" y1="14" x2="16.5" y2="14"/>
            </g>
          </svg>
          www.milofenwick.net
        </li>
      </ul>
    </div>
  </section>

</body>
</html>
```